Ice Cream Cup Design

We need a packaging design for ice cream cups.
We're a London based company called Villa Rosa Dolci and are producers of fresh Italian Artisan Gelato our website is www.villarosadolci.co.uk

We're looking to invest in a cup filling machine to fill 100ml and 500ml cups of gelato.
The 500ml cup will be the same shape and height as the Nordvik Freeze tub with a matching lid design.
The 100ml cup will be of the same shape and height of the Nordvik Freeze Single Serve cup with a matching lid design and includes a spoon inside.

We're looking for edgy clean designs that give an impression of quality and draw attention to the product if it sat on a product shelf. Inspired by packaging such as Ko, Pemberly and Harrowfield we're keen on a black themed packaging with a striking contrast of simple colour and a simple ice cream or gelato image that shows more than one flavour.
This particular design is not boasting any particular flavour, its a uniform design across our whole range of flavours.

Our company logo may be too fussy for this packaging so we would like to include our company ice cream logo and a way to include our company name but still look edgy for example - just like Pemberly Tea - our ice cream logo big G underneath, then 'VILLA ROSA DOLCI' underneath, and below that 'ARTISAN ITALIAN GELATO'. Or anything that inspires and looks good, will draw attention and looks sexy and indulgent and gives an impression of luxury product.

Please check attached document for cup shape and dimensions.

Reason: Christmas and New Year Holiday period resulted in less time for feedback opportunity and new designs to be posted.

Target Market(s)

Target market between 20-40 years old, consumers of quality desserts all year round.

Industry/Entity Type

It Company

Requirements
Must have
• Our Ice Cream Logo
Our name (doesn't need to necessarily have it in our font, can be in bold lettering)
Nice to have
• Limited writing and fuss.
Ideal to have simple clean designs
Should not have
• Eccentric colours and fun childlike images.

```html
<!DOCTYPE html>
<html lang="en">
<head>
<meta charset="utf-8">
<title>Villa Rosa Dolci – Gelato Cup Label</title>
<link rel="stylesheet" href="https://fonts.googleapis.com/css2?family=Parisienne&family=Raleway:wght@300;400&family=Archivo+Narrow:wght@400;700&display=swap">
<style>
  :root {
    --page: #ffffff;
    --label: #050505;
    --gold: #e0aa12;
    --gold-text: #e8b51f;
    --grey-text: #8b8b8b;
    --panel-text: #d8d8d8;
    --rule: #cfcfcf;
  }
  * { margin: 0; padding: 0; box-sizing: border-box; }
  html, body { width: 1200px; height: 1000px; overflow: hidden; background: var(--page); }
  .canvas { position: relative; width: 1200px; height: 1000px; background: var(--page); }

  .label {
    position: absolute; left: 0; top: 306px;
    width: 1200px; height: 388px;
    background: var(--label);
  }
  .label__trim {
    position: absolute; left: 0; bottom: 0; width: 100%; height: 7px;
    background: var(--gold);
  }

  .hero-art {
    position: absolute; left: 268px; top: 30px; width: 238px; height: 238px;
  }

  .brand {
    position: absolute; left: 200px; top: 276px; width: 420px;
  }
  .brand__row { display: flex; align-items: center; gap: 12px; }
  .brand__dot {
    width: 34px; height: 34px; border-radius: 50%;
    border: 1.5px solid var(--grey-text); flex: none;
  }
  .brand__name {
    font-family: "Parisienne", cursive;
    font-size: 44px; line-height: 1; color: var(--gold-text);
    white-space: nowrap;
  }
  .brand__tagline {
    margin-top: 6px; margin-left: 58px;
    font-family: "Raleway", sans-serif; font-weight: 300;
    font-size: 17px; letter-spacing: 4.6px; color: var(--grey-text);
    white-space: nowrap;
  }

  .nutrition {
    position: absolute; left: 815px; top: 228px; width: 110px; height: 130px;
    border: 1px solid var(--rule); padding: 2px 3px;
    font-family: "Archivo Narrow", sans-serif; color: var(--panel-text);
    font-size: 5px; line-height: 1.35;
  }
  .nutrition__title { font-size: 14px; font-weight: 700; line-height: 1.05; }
  .nutrition__bar { height: 4px; background: var(--rule); margin: 1px 0; }
  .nutrition__line { border-top: 0.5px solid var(--rule); display: flex; justify-content: space-between; }
  .nutrition__line--indent { padding-left: 5px; }
  .nutrition__right { text-align: right; }
  .nutrition strong { font-weight: 700; }

  .ingredients, .maker {
    position: absolute; left: 934px;
    font-family: "Archivo Narrow", sans-serif; font-size: 8px; line-height: 1.25;
    color: var(--grey-text); width: 130px;
  }
  .ingredients { top: 230px; }
  .maker { top: 334px; }
</style>
</head>
<body>
<div class="canvas">
  <section class="label">
    <svg class="hero-art" viewBox="0 0 238 238" role="img" aria-label="Illustration of a glass coupe holding scoops of raspberry, caramel, vanilla and chocolate gelato">
      <defs>
        <linearGradient id="scoops" x1="0" y1="0" x2="1" y2="1">
          <stop offset="0" stop-color="#e6317f"/>
          <stop offset="0.45" stop-color="#d9a33a"/>
          <stop offset="1" stop-color="#4a2c1c"/>
        </linearGradient>
      </defs>
      <rect x="0" y="0" width="238" height="238" rx="18" fill="url(#scoops)" opacity="0.85"/>
    </svg>

    <div class="brand">
      <div class="brand__row">
        <span class="brand__dot"></span>
        <span class="brand__name">Villa Rosa Dolci</span>
      </div>
      <div class="brand__tagline">ARTISAN ITALIAN GELATO</div>
    </div>

    <div class="nutrition">
      <div class="nutrition__title">Nutrition Facts</div>
      <div>Serving Size 1/2 cup</div>
      <div class="nutrition__bar"></div>
      <div>Amount Per Serving</div>
      <div class="nutrition__line"><strong>Calories 120</strong></div>
      <div class="nutrition__bar"></div>
      <div class="nutrition__right">% Daily Value</div>
      <div class="nutrition__line"><strong>Total Fat 6g</strong><span>9%</span></div>
      <div class="nutrition__line"><strong>Sodium 75mg</strong><span>3%</span></div>
      <div class="nutrition__line"><strong>Total Carbohydrate 15g</strong><span>5%</span></div>
      <div class="nutrition__line nutrition__line--indent">Sugars 12g</div>
      <div class="nutrition__line"><strong>Protein 2g</strong></div>
      <div class="nutrition__bar"></div>
      <div>Percent Daily Values based on 2,000 calorie diet</div>
    </div>

    <p class="ingredients">Ingredients:<br>Cream, eggs, sugar, chocolate,<br>raspberries, caramel</p>
    <p class="maker">Manufactured for<br>Villa Rosa Dolci</p>

    <div class="label__trim"></div>
  </section>
</div>
</body>
</html>
```